Bluvora business website

I am wanting a website for my media agency Bluvora.

It needs to be be an attractive, unique and professional looking website. The website is a destination for people to be able to understand the service that Bluvora offers.

Please read uploaded website copy to gain an understanding of the business.

Target Market(s)

small business owners, business decision makers, marketing managers,

Industry/Entity Type

Business

Requirements
Must have
• Good branding.

```html
<!DOCTYPE html>
<html lang="en">
<head>
<meta charset="utf-8">
<title>Bluvora – Media Strategy, Planning and Buying Agency</title>
<link href="https://fonts.googleapis.com/css2?family=Source+Sans+3:wght@300;400;600&display=swap" rel="stylesheet">
<style>
:root{
  --violet-top:#7d70f0;
  --violet-bottom:#4b3ce6;
  --brand:#3b2fe0;
  --title:#2a22a8;
  --ink:#555;
  --ink-dark:#444;
  --line:#e2e2e2;
  --white:#fff;
}
*{margin:0;padding:0;box-sizing:border-box}
html,body{width:931px;height:1200px;overflow:hidden;background:var(--white)}
body{position:relative;font-family:"Source Sans 3",sans-serif;color:var(--ink)}
.abs{position:absolute}
h1,h2,h3,strong{font-weight:400}

/* header */
.site-header{left:0;top:0;width:931px;height:60px;background:linear-gradient(#fff,#f1f1f1);border-bottom:1px solid #ddd}
.main-nav{left:310px;top:0;height:60px;display:flex}
.main-nav a{display:block;height:60px;line-height:64px;padding:0 18px;font-size:13.5px;color:#333;text-decoration:none;border-right:1px solid #ddd}
.main-nav a:last-child{border-right:none}
.social{left:769px;top:21px;display:flex;gap:2px}
.social span{width:22px;height:22px;border-radius:50%;background:#bdbdbd}

.brand-card{left:57px;top:0;width:138px;height:131px;background:var(--white);border-radius:0 0 4px 4px;z-index:2;display:flex;align-items:center;justify-content:center;gap:7px}
.brand-square{width:14px;height:14px;background:var(--brand)}
.brand-name{font-weight:600;font-size:24px;color:var(--brand)}

/* hero */
.hero{left:0;top:60px;width:931px;height:348px;background:linear-gradient(var(--violet-top),var(--violet-bottom))}
.hero-title{left:57px;top:96px;color:var(--white);font-weight:300;font-size:25px;line-height:1.2}
.hero-title strong{display:block;font-size:31px;margin-top:2px}
.hero-text{left:57px;top:172px;width:350px;color:var(--white);font-size:10.5px;line-height:19px;font-weight:400}
.dots{left:59px;top:239px;display:flex;gap:2px}
.dots span{width:11px;height:11px;border-radius:50%;background:#8f86f0}
.dots span:first-child{background:var(--white)}
.video-frame{left:477px;top:40px;width:396px;height:262px;background:var(--white);padding:6px 6px 0}
.video-image{width:384px;height:256px;background:linear-gradient(#b56a5a 0%,#6f8fa8 30%,#c6a888 55%,#eceae6 85%,#fff)}
.play{left:180px;top:112px}

/* welcome */
.welcome-title{left:0;width:931px;top:448px;text-align:center;font-weight:300;font-size:29px;color:var(--ink-dark)}
.welcome-text{left:88px;width:755px;top:489px;text-align:center;font-size:10.3px;line-height:19.5px;font-weight:300;color:var(--ink)}
.welcome-text p+p{margin-top:3px}
.btn-grey{left:412px;top:586px;width:106px;height:32px;line-height:32px;text-align:center;background:linear-gradient(#ececec,#d6d6d6);border-radius:2px;font-size:14px;color:#666}
.divider{left:57px;top:663px;width:815px;height:1px;background:var(--line)}

/* services */
.section-title{left:0;width:931px;top:686px;text-align:center;font-weight:300;font-size:29px;color:var(--ink-dark)}
.section-sub{left:0;width:931px;top:725px;text-align:center;font-size:12.5px;font-weight:300;color:var(--ink-dark)}
.card{top:763px;width:259px;height:303px;border:1px solid var(--line);border-radius:3px;box-shadow:0 1px 2px rgba(0,0,0,.05)}
.card-image{position:absolute;left:14px;top:10px;width:230px;height:116px}
.card-title{position:absolute;left:0;width:100%;top:134px;text-align:center;color:var(--title);font-size:14.5px;line-height:19px}
.card-text{position:absolute;left:26px;right:26px;text-align:center;font-size:10.8px;line-height:19.2px;font-weight:300;color:var(--ink)}
.btn-blue{position:absolute;left:88px;top:258px;width:81px;height:24px;line-height:24px;text-align:center;background:var(--brand);color:var(--white);font-size:10.5px;border-radius:2px}

/* footer */
.site-footer{left:0;top:1114px;width:931px;height:86px;background:linear-gradient(#f4f4f4,#fff)}
.copyright{left:68px;top:27px;font-size:10.5px;font-weight:300;color:#666}
.footer-nav{right:67px;top:25px;font-size:12.5px;color:#333}
.footer-nav span{margin:0 5px;color:#666}
</style>
</head>
<body>

<header class="abs site-header">
  <nav class="abs main-nav">
    <a>HOME</a><a>ABOUT US</a><a>WHAT WE DO</a><a>IDEAS</a><a>CONTACT</a>
  </nav>
  <div class="abs social"><span></span><span></span><span></span><span></span></div>
</header>

<div class="abs brand-card">
  <span class="brand-square"></span><span class="brand-name">Bluvora</span>
</div>

<section class="abs hero">
  <h1 class="abs hero-title">Bluvora is a Media Strategy,<strong>Planning and Buying Agency.</strong></h1>
  <p class="abs hero-text">Duis tincidunt lectus quis dui viverra vestibulum. Suspendisse vulputate aliquam dui. Nulla elementum dui ut augue. Aliquam vehicula mi at mauris. Maecenas placerat, nisl at consequat rhoncus</p>
  <div class="abs dots"><span></span><span></span><span></span><span></span></div>
  <div class="abs video-frame">
    <div class="video-image" role="img" aria-label="Curved wall of colourful photo tiles, video preview"></div>
    <svg class="abs play" width="42" height="42" viewBox="0 0 42 42" aria-hidden="true">
      <circle cx="21" cy="21" r="20" fill="#fff"/>
      <path d="M16 12 L30 21 L16 30 Z" fill="#111"/>
    </svg>
  </div>
</section>

<h2 class="abs welcome-title">Welcome to Our Website Mainpage..</h2>
<div class="abs welcome-text">
  <p>Bluvora works across all offline platforms (radio, press, outdoor &amp; TV), search engine marketing, online display, email, social &amp; mobile. We attain a high level of value for our clients with a focus on integration. We are marketing partners in our clients businesses and enjoy seeing them grow and achieve their goals.</p>
  <p>Vivamus porttitor, g, purus nisi eleifend libero, a tempus libero lectus feugiat felis. Morbi diam mauris, viverra in, gravida eu, mattis in, ante. Morbi eget arcu. Morbi porta, libero id ullamcorper nonummy, nibh ligula pulvinar metus, eget consectetuer augue nisi quis lacus</p>
</div>
<div class="abs btn-grey">Learn More</div>
<div class="abs divider"></div>

<h2 class="abs section-title">What We Do</h2>
<p class="abs section-sub">Vivamus porttitor, g, purus nisi eleifend libero, a tempus libero lectus feugiat felis. Morbi diam mauris, viverra in, gravida eu</p>

<article class="abs card" style="left:54px">
  <div class="card-image" role="img" aria-label="Tablet showing business charts on a desk" style="background:linear-gradient(135deg,#dfe8f2,#9fb2c8 45%,#2d2d33 60%,#eef1f5)"></div>
  <h3 class="card-title">Media Strategy &amp; Planning</h3>
  <p class="card-text" style="top:159px">Using accurate analysis we provide relevant research about the consumer or business target &amp; trends in the market place. A tailored strategy is devised that com-prises of the right media channels</p>
  <div class="btn-blue">Learn More</div>
</article>

<article class="abs card" style="left:330px">
  <div class="card-image" role="img" aria-label="Business people in a video conference meeting" style="background:linear-gradient(90deg,#2a2a2e,#a9c6c0 40%,#d8e2dc 60%,#2c2c30)"></div>
  <h3 class="card-title">Media Trading &amp; Campaign<br>Monitoring</h3>
  <p class="card-text" style="top:178px">Using our media partner relationships, trade negotiation techniques &amp; experience we achieve a high level of value for all media buys that leads</p>
  <div class="btn-blue">Learn More</div>
</article>

<article class="abs card" style="left:604px">
  <div class="card-image" role="img" aria-label="Illustrated city of screens and devices with content icons" style="background:linear-gradient(#c9dbe8,#e4ecf1 45%,#8a8f99 75%,#5c6470)"></div>
  <h3 class="card-title">Content &amp; Creative</h3>
  <p class="card-text" style="top:159px">Creating imaginative &amp; interesting content for a brand can be a great way of achieving a high level of engagement to a target audience. Content can be published and broadcast on a variety of different media</p>
  <div class="btn-blue">Learn More</div>
</article>

<footer class="abs site-footer">
  <p class="abs copyright">© 2013 Company Name.&nbsp; All right reserved.&nbsp; Term of Use</p>
  <nav class="abs footer-nav">HOME<span>|</span>ABOUT US<span>|</span>WHAT WE DO<span>|</span>IDEAS<span>|</span>CONTACT</nav>
</footer>

</body>
</html>
```